DL Flyer announcing opening of Thistle Fern Row Homewares & Gift Store

To create 2 sided full colour DL Flyer which will be distributed by a letterbox drop to announce the opening of a delightful new homewares and gift store called "Thistle Fern Row Homewares" at 87 Marlowe Creek Road, Ashcombe.

Thistle Fern Row Homewares offers a range of exclusive, bespoke, well-crafted decorative homewares and gifts. Our target market is well to do and aspirational, so we want the design of the flyer to match.

The owners, Brenda (a long-time resident of Ashcombe) and Lorna have combined their love of homewares and years of retail experience to create this fresh and exciting new store.

Thistle Fern Row will cater for all those special occasions throughout the year but right now as we move into Christmas we have some beautiful Christmas decorations. Why not come in and visit Lorna who has 18 years experience in the Christmas industry and find out about our Christmas Tree decorating service.

Also we want a call to action so want to offer a 10% discount for people who bring the flyer in during the month of November

The store is open Tuesday to Friday 9.30am to 5.00pm and Saturday 10.00am to 4.00pm

Please find attached duck design we are using the coloured version (excluding the word 'duck' of course). The colour we have chosen for Thistle Fern Row is "Duck Egg Blue" and the font is Lucida Calligraphy.

Thank you

Target Market(s)

is well to do and aspirational

Industry/Entity Type

Store

• Lucida Calligraphy

Colors
cfeae6

Requirements
Must have
• the Duck. Discount voucher, address, look forward to being of service for many years to come. "Duck Egg Blue" colour tones

```html
<!DOCTYPE html>
<html lang="en">
<head>
<meta charset="utf-8">
<title>Thistle Fern Row Homewares – DL Flyer</title>
<link rel="stylesheet" href="https://fonts.googleapis.com/css2?family=Merienda:wght@400;700&family=Playfair+Display:wght@400;700&display=swap">
<style>
  :root {
    --duck-egg: #cfeae6;
    --duck-egg-deep: #bfe3da;
    --ink: #2f3a38;
    --paper: #ffffff;
    --accent-mint: #a9dccb;
    --stage: #f4f4f1;
    --duck-white: #ecebe8;
  }
  * { box-sizing: border-box; margin: 0; padding: 0; }
  html, body {
    width: 1139px; height: 1200px; overflow: hidden;
    background: var(--stage);
  }
  .canvas { position: relative; width: 1139px; height: 1200px; }

  .flyer {
    position: absolute; left: 70px; width: 1000px; height: 470px;
    background: repeating-linear-gradient(90deg, var(--duck-egg) 0 14px, var(--duck-egg-deep) 14px 20px);
    overflow: hidden;
    box-shadow: 0 4px 14px rgba(0,0,0,.12);
    font-family: "Merienda", cursive;
    color: var(--ink);
  }
  .flyer--front { top: 50px; }
  .flyer--back { top: 640px; }

  .hanging-sign { position: absolute; left: 0; top: 0; width: 280px; height: 300px; }

  .cartouche {
    position: absolute; background: var(--paper);
    border: 3px solid var(--ink); border-radius: 38% / 30%;
    display: flex; align-items: center; justify-content: center;
  }
  .flyer--front .cartouche { left: 40px; top: 130px; width: 210px; height: 150px; }
  .flyer--back .cartouche { left: 345px; top: 60px; width: 310px; height: 230px; }
  .duck-illustration {
    width: 58%; height: 70%; border-radius: 45% 45% 40% 40%;
    background: radial-gradient(ellipse at 55% 45%, var(--duck-white) 0%, #dcdad6 70%, var(--paper) 100%);
  }

  .store-name { font-size: 33px; font-weight: 400; letter-spacing: .5px; white-space: nowrap; }
  .flyer--front .store-name { position: absolute; left: 55px; top: 305px; }
  .tagline { position: absolute; left: 110px; top: 357px; font-size: 17px; font-style: italic; white-space: nowrap; }
  .address {
    position: absolute; left: 55px; top: 412px; font-size: 20px;
    display: flex; align-items: center; gap: 10px; white-space: nowrap;
  }
  .address svg { width: 18px; height: 22px; }

  .hours {
    position: absolute; left: 390px; top: 66px; width: 300px; height: 96px;
    background: var(--paper); border: 1.5px solid var(--accent-mint);
    border-radius: 10px; text-align: center; padding-top: 12px;
  }
  .hours__title { font-size: 17px; margin-bottom: 6px; }
  .hours__row { font-size: 12px; line-height: 1.6; white-space: nowrap; }
  .hours__pin {
    position: absolute; left: 50%; top: -36px; width: 8px; height: 8px;
    margin-left: -4px; border-radius: 50%; background: var(--ink);
  }

  .discount { position: absolute; left: 610px; top: 150px; width: 440px; height: 440px; }

  .flyer--back .store-name {
    position: absolute; left: 0; right: 0; top: 345px; text-align: center; font-size: 34px;
  }
</style>
</head>
<body>
<main class="canvas">

  <section class="flyer flyer--front" aria-label="Flyer front">
    <svg class="hanging-sign" viewBox="0 0 280 300" aria-hidden="true">
      <line x1="0" y1="55" x2="225" y2="55" stroke="var(--ink)" stroke-width="3"/>
      <circle cx="230" cy="55" r="6" fill="var(--ink)"/>
      <line x1="50" y1="55" x2="50" y2="138" stroke="var(--ink)" stroke-width="2.5" stroke-dasharray="5 3"/>
      <line x1="190" y1="55" x2="190" y2="138" stroke="var(--ink)" stroke-width="2.5" stroke-dasharray="5 3"/>
    </svg>
    <div class="cartouche">
      <div class="duck-illustration" role="img" aria-label="Illustration of a white duck with orange beak and feet"></div>
    </div>
    <h1 class="store-name">"Thistle Fern Row Homewares"</h1>
    <p class="tagline">- exclusive decorative homewares and gifts -</p>
    <p class="address">
      <svg viewBox="0 0 18 22" aria-hidden="true"><path d="M9 1a7 7 0 0 0-7 7c0 5 7 13 7 13s7-8 7-13a7 7 0 0 0-7-7z" fill="none" stroke="var(--ink)" stroke-width="2"/><circle cx="9" cy="8" r="2.5" fill="var(--ink)"/></svg>
      87 Marlowe Creek Road, Ashcombe
    </p>

    <div class="hours">
      <span class="hours__pin"></span>
      <p class="hours__title">Store is open</p>
      <p class="hours__row">Tuesday – Friday &nbsp; 9.00 am – 5.30 pm</p>
      <p class="hours__row">Saturday &nbsp; 9.30 am – 3.30 pm</p>
    </div>

    <svg class="discount" viewBox="0 0 440 440" aria-label="10% discount with the flyer during the month of November">
      <defs><path id="discount-arc" d="M85 200 A135 135 0 0 1 355 200"/></defs>
      <circle cx="220" cy="220" r="205" fill="var(--paper)" stroke="var(--accent-mint)" stroke-width="2"/>
      <text font-family="Merienda, cursive" font-size="21" fill="var(--ink)">
        <textPath href="#discount-arc" startOffset="50%" text-anchor="middle">discount with the flyer</textPath>
      </text>
      <text x="220" y="205" text-anchor="middle" font-family="Playfair Display, serif" font-size="74" font-weight="700" fill="var(--ink)">10<tspan font-size="42" font-weight="400">%</tspan></text>
      <line x1="105" y1="232" x2="335" y2="232" stroke="var(--accent-mint)" stroke-width="1.5"/>
      <text x="220" y="264" text-anchor="middle" font-family="Merienda, cursive" font-size="17" fill="var(--ink)">during the month of November</text>
    </svg>
  </section>

  <section class="flyer flyer--back" aria-label="Flyer back">
    <div class="cartouche">
      <div class="duck-illustration" role="img" aria-label="Illustration of a white duck with orange beak and feet"></div>
    </div>
    <h2 class="store-name">"Thistle Fern Row Homewares"</h2>
  </section>

</main>
</body>
</html>
```